Quick turn around Concierge Business Tri-Fold Brochure Modern & Classy

Vacation, Personal, Homeowners and Business Concierge Services company. I just started this company. I have a logo and am working on my website. I have attached a list of our services. I like the color blue and i am based on a beach so Vacationers and Rental Homeowners are my target audience. Logo attached as well. The article gives examples

Target Market(s)

Vacationers, Rental Home Owners & Agents, Individuals

Industry/Entity Type

Hospitality

Font styles to use
Serif
Sans Serif

Colors
0592cd

Requirements
Must have
• Contact information & logo
• Partial list of services
• Tri-Fold design

```html
<!DOCTYPE html>
<html lang="en">
<head>
<meta charset="utf-8">
<title>Shoreline Concierge Services – Tri-Fold Brochure</title>
<link rel="stylesheet" href="https://fonts.googleapis.com/css2?family=Allura&family=Arimo:wght@400;700&family=Montserrat:wght@600;800&display=swap">
<style>
  :root {
    --stage: #3b3d40;
    --brand-blue: #1f9ad6;
    --deep-blue: #0b6fa6;
    --navy: #1b2a3a;
    --white: #ffffff;
    --sky-top: #8fd0f0;
    --sea: #2ec4d6;
    --sea-deep: #0f8fb8;
    --palm-light: #9fd34a;
    --palm-dark: #3f8f2a;
  }
  * { box-sizing: border-box; margin: 0; padding: 0; }
  html, body {
    width: 1200px; height: 828px; overflow: hidden;
    background: var(--stage);
  }
  .brochure {
    position: absolute; left: 20px; top: 14px;
    width: 1160px; height: 800px;
    overflow: hidden;
    background: var(--brand-blue);
    color: var(--white);
    font-family: "Arimo", Arial, sans-serif;
  }
  .brochure-art { position: absolute; inset: 0; width: 1160px; height: 800px; }
  .panel {
    position: absolute; top: 0; height: 800px;
  }
  .panel--front { left: 0; width: 387px; }
  .panel--inside { left: 387px; width: 386px; }
  .panel--back { left: 773px; width: 387px; }
  .fold-line {
    position: absolute; top: 0; width: 1px; height: 800px;
    background: rgba(0, 0, 0, 0.08);
  }

  .brand {
    position: absolute; left: 26px; top: 22px;
    display: flex; align-items: center; gap: 12px;
    white-space: nowrap;
  }
  .brand-square {
    width: 30px; height: 30px; background: var(--navy);
  }
  .brand-name {
    font-family: "Montserrat", Arial, sans-serif;
    font-weight: 600; font-size: 33px; color: var(--navy);
    letter-spacing: -0.3px;
  }
  .tagline {
    position: absolute; left: 300px; top: 66px;
    font-family: "Arimo", Arial, sans-serif; font-weight: 700;
    font-size: 14px; color: var(--navy); white-space: nowrap;
  }

  .headline {
    position: absolute; left: 60px; top: 420px; width: 310px;
    font-family: "Montserrat", Arial, sans-serif; font-weight: 800;
    font-size: 28px; line-height: 32px; text-transform: uppercase;
    text-align: right; letter-spacing: 0.5px;
  }
  .front-copy {
    position: absolute; left: 24px; top: 492px; width: 340px;
  }
  .script-heading {
    font-family: "Allura", cursive;
    font-weight: 400; font-size: 30px; line-height: 32px;
    color: var(--white);
  }
  .script-heading--ruled {
    border-bottom: 1px solid rgba(255,255,255,0.7);
    padding-bottom: 2px; margin-bottom: 6px;
  }
  .body-copy {
    font-size: 11.5px; line-height: 14px; margin-bottom: 6px;
  }

  .service-column { position: absolute; }
  .panel--inside .service-column { left: 26px; top: 318px; width: 340px; }
  .panel--back .service-column { left: 30px; top: 22px; width: 330px; }
  .service-group { margin-bottom: 8px; }
  .service-list { list-style: none; font-size: 12px; line-height: 15px; }
  .service-note { font-size: 12px; line-height: 15px; }
</style>
</head>
<body>
<main class="brochure">
  <svg class="brochure-art" viewBox="0 0 1160 800" xmlns="http://www.w3.org/2000/svg" aria-hidden="false">
    <defs>
      <linearGradient id="photoTones" x1="0" y1="0" x2="0" y2="1">
        <stop offset="0" stop-color="var(--sky-top)"/>
        <stop offset="0.45" stop-color="#cfeaf5"/>
        <stop offset="0.55" stop-color="var(--sea)"/>
        <stop offset="1" stop-color="var(--sea-deep)"/>
      </linearGradient>
      <linearGradient id="palmTones" x1="0" y1="1" x2="1" y2="0">
        <stop offset="0" stop-color="var(--palm-dark)"/>
        <stop offset="1" stop-color="var(--palm-light)"/>
      </linearGradient>
    </defs>
    <rect x="0" y="0" width="773" height="96" fill="var(--white)"/>
    <path d="M0,96 H773 V104 Q640,320 430,345 Q210,372 0,404 Z" fill="url(#photoTones)"
          role="img" aria-label="Photo of a tropical lagoon with overwater bungalows, a green island peak and palm fronds in the foreground"/>
    <path d="M773,104 Q640,320 430,345 Q210,372 0,404" fill="none" stroke="var(--white)" stroke-width="6"/>
    <path d="M773,748 Q960,730 1160,612 V800 H773 Z" fill="var(--white)"/>
    <path d="M900,800 Q950,680 1060,640 Q1120,620 1160,560 V800 Z" fill="url(#palmTones)" opacity="0.9"
          role="img" aria-label="Palm fronds rising from the lower corner"/>
  </svg>

  <span class="fold-line" style="left:387px"></span>
  <span class="fold-line" style="left:773px"></span>

  <section class="panel panel--front">
    <div class="brand">
      <span class="brand-square"></span>
      <span class="brand-name">Shoreline Concierge Services</span>
    </div>
    <h1 class="headline">Your life just got a whole lot easier</h1>
    <div class="front-copy">
      <h2 class="script-heading">About Us</h2>
      <p class="body-copy">Shoreline Concierge Services is a full service lifestyle company based on the coast. We take care of the details of daily life so you can spend your time on the things that matter most, whether you live here all year or visit for the season.</p>
      <p class="body-copy">We bring a caring attitude and a personal approach to every task. No job is too big or too small, and we are ready to help with a smile.</p>
      <h2 class="script-heading">Personal Assistant</h2>
      <p class="body-copy">Let us run your errands, manage your calendar and handle the tasks that fill your week. From a single request to ongoing support, we work around your schedule so you can enjoy more free time at home or away.</p>
    </div>
  </section>

  <section class="panel panel--inside">
    <p class="tagline" style="left:-87px">Your Life. Our Time.</p>
    <div class="service-column">
      <div class="service-group">
        <h2 class="script-heading">Home Services</h2>
        <ul class="service-list">
          <li>Property Maintenance</li>
          <li>Home organization projects</li>
          <li>Gather and present home improvement estimates</li>
          <li>Manage repair and construction projects</li>
          <li>Relocation packing/moving assistance/unpacking</li>
          <li>Attic &amp; garage clean out</li>
          <li>Liaison with home vendors (plumbers, electrician, cable, etc.)</li>
          <li>House sitting: check mail, water plants, peace of mind</li>
          <li>Mail management</li>
          <li>Landscaping/tree service/yard cleanup</li>
          <li>Preparations for House Guests</li>
        </ul>
      </div>
      <div class="service-group">
        <h2 class="script-heading">Office</h2>
        <ul class="service-list">
          <li>Corporate event planning</li>
          <li>Employee recognition program</li>
          <li>Arrange outside services</li>
          <li>Coordinate parties &amp; plan special events</li>
          <li>Incentive/recognition packages</li>
          <li>Computer Rental &amp; Repair</li>
          <li>Professional Speakers</li>
        </ul>
      </div>
      <div class="service-group">
        <h2 class="script-heading">Scheduling Appointments</h2>
        <ul class="service-list">
          <li>Doctors</li>
          <li>Spa</li>
          <li>Golf</li>
          <li>Home repair</li>
          <li>Estimates</li>
        </ul>
      </div>
    </div>
  </section>

  <section class="panel panel--back">
    <div class="service-column">
      <div class="service-group">
        <h2 class="script-heading script-heading--ruled">Local Errand Services</h2>
        <p class="service-note">Local island area free</p>
        <p class="service-note">*24 Hour emergency services available</p>
        <ul class="service-list" style="margin-top:8px">
          <li>Grocery Shopping</li>
          <li>Dry cleaning</li>
          <li>Prescription pick up</li>
          <li>Post office &amp; mailing</li>
          <li>Grocery shopping</li>
          <li>Personal shopping</li>
          <li>Returns</li>
        </ul>
      </div>
      <div class="service-group">
        <h2 class="script-heading script-heading--ruled">Referrals / Recommendations</h2>
        <ul class="service-list">
          <li>Personal trainers/tutors</li>
          <li>Home repair/handyman</li>
          <li>Interior design</li>
          <li>Pet sitting/walking</li>
          <li>Massage therapy</li>
          <li>Nanny &amp; child care</li>
        </ul>
      </div>
      <div class="service-group">
        <h2 class="script-heading script-heading--ruled">Reminder Service</h2>
        <ul class="service-list">
          <li>Anniversaries</li>
          <li>Birthdays</li>
          <li>Appointments</li>
        </ul>
      </div>
      <div class="service-group">
        <h2 class="script-heading script-heading--ruled">Entertainment &amp; Leisure</h2>
        <ul class="service-list">
          <li>Restaurant reservations</li>
          <li>Music lessons</li>
          <li>Theatre</li>
          <li>Sporting events</li>
          <li>Special events</li>
          <li>Tee Times/Green fees</li>
          <li>Tours</li>
          <li>Museums</li>
          <li>Tickets to popular shows</li>
          <li>Private Wine tasting &amp; Lectures</li>
        </ul>
      </div>
    </div>
  </section>
</main>
</body>
</html>
```